Emergency Medical Training and Events Company Business Needs Business Card Design

We are in need of a business card for our dynamic company expanding its customer base and need to be easily contacted and identified for when we visit with government officials, potential EMS / Fire agencies and county coordinators to arrange for training programs for first responders to better prepare them for critical thinking at critical incidents.

Target Market(s)

EMS/Fire and Event Promoters

Industry/Entity Type

Medical

Contact Information for Business Card

Two cards, comparable designs:

Martin K. Halvey, Principal, m.halvey@rvqtlo.com
Owen Tash, Event and Training Specialist, o.tash@rvqtlo.com

Font styles to use
Other font styles liked:
• Cambria

Colors

Designer to choose colors to be used in the design.

Requirements
Must have
• Company Logo, Spots for Name, Title, Phone Number, Email, Website
• A bullet list stating that we offer, QRB CPR and First Aid Instructors, Hold the Line Instructors, Event EMS, CME's, MCI Training and Planning. We prefer to have a black background for the card but if you can make a blue or white card stand out we would review that as well.
Should not have
• Tacky logos or special sayings ... simple, elegant, professional is the look we seek

```html
<!DOCTYPE html>
<html lang="en">
<head>
<meta charset="utf-8">
<title>Ravenquill TLO – Business Card</title>
<link href="https://fonts.googleapis.com/css2?family=Caladea:wght@700&family=Work+Sans:wght@400;500;700&display=swap" rel="stylesheet">
<style>
  :root {
    --backdrop: #1c1c1c;
    --card: #262626;
    --card-edge: #2e2e2e;
    --red: #d81f26;
    --white: #f4f4f4;
  }
  * { box-sizing: border-box; margin: 0; padding: 0; }
  html, body { width: 1200px; height: 900px; overflow: hidden; }
  body {
    background: var(--backdrop);
    font-family: "Work Sans", Arial, sans-serif;
    color: var(--white);
    position: relative;
  }
  .card {
    position: absolute;
    left: 250px;
    width: 700px;
    height: 400px;
    background: linear-gradient(135deg, var(--card) 0%, var(--card-edge) 100%);
    border-bottom: 8px solid var(--red);
    box-shadow: 0 12px 30px rgba(0,0,0,.55);
  }
  .card--services { top: 35px; }
  .card--contact { top: 470px; }

  .brand { display: flex; align-items: center; gap: 12px; white-space: nowrap; }
  .brand__dot { border-radius: 50%; background: var(--red); flex: none; }
  .brand__name { font-weight: 700; color: var(--white); line-height: 1; letter-spacing: .5px; }

  /* services side */
  .card--services .brand { position: absolute; left: 48px; top: 180px; }
  .card--services .brand__dot { width: 40px; height: 40px; }
  .card--services .brand__name { font-size: 25px; }
  .divider { position: absolute; width: 3px; background: var(--red); }
  .card--services .divider { left: 340px; top: 130px; height: 140px; }
  .services {
    position: absolute; left: 368px; top: 132px;
    list-style: none; font-size: 17px; font-weight: 500; line-height: 27px; white-space: nowrap;
  }
  .services li { position: relative; padding-left: 22px; }
  .services li::before {
    content: ""; position: absolute; left: 0; top: 9px;
    width: 9px; height: 9px; border-radius: 50%; background: var(--red);
  }

  /* contact side */
  .card--contact .brand { position: absolute; left: 0; right: 0; top: 78px; justify-content: center; gap: 14px; }
  .card--contact .brand__dot { width: 84px; height: 84px; }
  .card--contact .brand__name { font-size: 52px; }
  .person { position: absolute; right: 390px; top: 250px; text-align: right; white-space: nowrap; }
  .person__name {
    font-family: "Caladea", Cambria, Georgia, serif; font-weight: 700;
    color: var(--red); font-size: 32px; text-transform: uppercase; letter-spacing: .5px;
  }
  .person__title { font-size: 20px; margin-top: 2px; letter-spacing: .5px; }
  .card--contact .divider { left: 340px; top: 250px; height: 110px; }
  .contacts { position: absolute; left: 370px; top: 245px; list-style: none; font-size: 19px; line-height: 29px; letter-spacing: .5px; white-space: nowrap; }
  .contacts li { display: flex; align-items: center; gap: 10px; }
  .contacts svg { width: 14px; height: 14px; flex: none; }
</style>
</head>
<body>
  <section class="card card--services">
    <div class="brand"><span class="brand__dot"></span><span class="brand__name">Ravenquill TLO</span></div>
    <span class="divider"></span>
    <ul class="services">
      <li>QRB CPR and First Aid Instructors</li>
      <li>Hold the Line Instructors</li>
      <li>Event EMS</li>
      <li>CMEs</li>
      <li>MCI Training and Planning</li>
    </ul>
  </section>

  <section class="card card--contact">
    <div class="brand"><span class="brand__dot"></span><span class="brand__name">Ravenquill TLO</span></div>
    <div class="person">
      <p class="person__name">Martin K. Halvey</p>
      <p class="person__title">Principal</p>
    </div>
    <span class="divider"></span>
    <ul class="contacts">
      <li><svg viewBox="0 0 16 16" aria-hidden="true"><path d="M4 1l3 3-2 2c1 2 3 4 5 5l2-2 3 3-2 2C7 14 2 9 2 3z" fill="#d81f26"/></svg>555.014.2290</li>
      <li><svg viewBox="0 0 16 16" aria-hidden="true"><rect x="4" y="1" width="8" height="14" rx="1.5" fill="none" stroke="#d81f26" stroke-width="1.6"/><circle cx="8" cy="12.5" r="1" fill="#d81f26"/></svg>555.018.4471</li>
      <li><svg viewBox="0 0 16 16" aria-hidden="true"><rect x="1" y="3" width="14" height="10" fill="none" stroke="#d81f26" stroke-width="1.6"/><path d="M1 3l7 6 7-6" fill="none" stroke="#d81f26" stroke-width="1.6"/></svg>m.halvey@rvqtlo.com</li>
      <li><svg viewBox="0 0 16 16" aria-hidden="true"><circle cx="8" cy="8" r="6.5" fill="none" stroke="#d81f26" stroke-width="1.4"/><ellipse cx="8" cy="8" rx="3" ry="6.5" fill="none" stroke="#d81f26" stroke-width="1.2"/><path d="M1.5 8h13" stroke="#d81f26" stroke-width="1.2"/></svg>www.rvqtlo.com</li>
    </ul>
  </section>
</body>
</html>
```